Book Cover Design Project - SIMPLE ART, Pre-Concepted

We already have a full design concept for the cover art. It is however in a low quality word document format. This project is to recreate existing example guideline art in as much vector art possible for great quality print production. Artistic flare is welcome. This will be for a book cover (front/back) and I want the quality to be excellent.

Art to be provided in Adobe Illustrator format. The book will be 6wide x 9high, so the artboard for the cover needs to be set up to 12.5 wide x 9 high with .125" bleeds.

Copy content for the spine: "Beneath a Copper Evening Sky Still" RL Moskowicz.

Here is a link to download the word document "template" and a new photo for the back page. I'm not sure that I like the new photo, it is possible the old one in the word document will work.

www.bluemarlinpressworks.com/uploads/QuillHavenSharedFiles.zip

I've got a fast deadline on this project because the client would like to have manufacturing completed by Christmas...which is why this is only a 2 day project. I appreciate your interest in our project.

Gordon

Try this link...seems I was missing the .zip extension which may have been causing problems.

Requirements
Must have
• Adobe Illustrator Files
CMYK color setup - no color definitions for project
Artboard Size: 12.625 wide x 9.125 high
Art Orientation: Flat image should have the back book page on the left side, front page on the right side, spine copy running down the middle.

```html
<!DOCTYPE html>
<html lang="en">
<head>
<meta charset="utf-8">
<title>Beneath a Copper Evening Sky Still — Cover</title>
<link rel="stylesheet" href="https://fonts.googleapis.com/css2?family=Jost:wght@300;600&family=Rye&display=swap">
<style>
  :root {
    --sky-light: #eef0f3;
    --sky-mid: #b9bfc9;
    --sky-deep: #6f7684;
    --panel: rgba(88, 94, 112, 0.86);
    --panel-text: #f4f5f8;
    --title-red: #e3232c;
    --ink: #111111;
    --cross: #0c0c0c;
    --trim: #3a3a3a;
    --photo: #8a7a6c;
  }
  * { margin: 0; padding: 0; box-sizing: border-box; }
  html, body { width: 1200px; height: 869px; overflow: hidden; background: #ffffff; }
  .cover {
    position: relative;
    width: 1200px;
    height: 869px;
    overflow: hidden;
    font-family: "Jost", "Futura", sans-serif;
  }
  .sky {
    position: absolute;
    inset: 0;
    background:
      radial-gradient(ellipse 40% 30% at 20% 80%, rgba(255,255,255,0.9), transparent 70%),
      radial-gradient(ellipse 35% 25% at 75% 45%, rgba(255,255,255,0.85), transparent 70%),
      radial-gradient(ellipse 45% 35% at 90% 70%, rgba(70,76,88,0.7), transparent 70%),
      radial-gradient(ellipse 30% 25% at 60% 10%, rgba(90,96,108,0.55), transparent 70%),
      linear-gradient(180deg, var(--sky-mid) 0%, var(--sky-light) 45%, var(--sky-mid) 75%, var(--sky-deep) 100%);
  }
  .trim-frame {
    position: absolute;
    inset: 8px;
    border: 1px solid var(--trim);
    pointer-events: none;
  }
  .fold {
    position: absolute;
    top: 0;
    bottom: 0;
    border-left: 1px dashed var(--trim);
  }
  .fold--left { left: 568px; }
  .fold--right { left: 623px; }

  /* Back cover */
  .back-panel {
    position: absolute;
    left: 59px;
    top: 0;
    width: 502px;
    height: 719px;
    background: var(--panel);
    color: var(--panel-text);
    padding: 54px 14px 0 23px;
    font-size: 11.3px;
    line-height: 15.6px;
    font-weight: 300;
    text-align: justify;
  }
  .author-photo {
    float: left;
    width: 171px;
    height: 198px;
    margin: 0 15px 4px 0;
    background: linear-gradient(160deg, #b7a897 0%, var(--photo) 55%, #2d2f38 100%);
  }
  .bio-lead { font-weight: 600; margin-bottom: 12px; }
  .bio p + p { margin-top: 15px; }

  /* Spine */
  .spine {
    position: absolute;
    left: 569px;
    top: 0;
    width: 54px;
    height: 869px;
  }
  .spine-title, .spine-author {
    position: absolute;
    left: 50%;
    writing-mode: vertical-rl;
    transform: translateX(-50%);
    font-family: "Rye", "Georgia", serif;
    white-space: nowrap;
  }
  .spine-title { top: 52px; font-size: 21px; color: var(--title-red); letter-spacing: 0.5px; }
  .spine-author { top: 622px; font-size: 20px; color: var(--ink); }

  /* Front cover */
  .front-title {
    position: absolute;
    font-family: "Rye", "Georgia", serif;
    color: var(--title-red);
    text-shadow: 0 0 2px rgba(255,255,255,0.6);
    white-space: nowrap;
  }
  .title-top { left: 623px; width: 577px; top: 56px; text-align: center; font-size: 41px; }
  .title-left { right: 398px; top: 231px; font-size: 36px; }
  .title-right { left: 1012px; top: 231px; font-size: 36px; }
  .title-bottom { left: 623px; width: 577px; top: 548px; text-align: center; font-size: 50px; }
  .cross { position: absolute; left: 815px; top: 114px; }
  .tagline {
    position: absolute;
    left: 623px;
    width: 577px;
    top: 799px;
    text-align: center;
    font-family: "Rye", "Georgia", serif;
    font-size: 15px;
    color: var(--ink);
    letter-spacing: 0.5px;
  }
</style>
</head>
<body>
<div class="cover">
  <div class="sky" role="img" aria-label="Photograph of a cloudy grey and white sky spanning the whole cover"></div>

  <section class="back-panel">
    <div class="author-photo" role="img" aria-label="Portrait photograph of the author in a dark suit"></div>
    <div class="bio">
      <p class="bio-lead">About the author: The word of God says that “I know the plans I have for you” (Jeremiah 29:11) and that “before I formed you in the womb I knew you” (Jeremiah 1:15). These verses of scripture depict the life of Raymond L Moskowicz.</p>
      <p>As a little boy Raymond was always told that he was going to be a preacher. The magnitude of this repeated statement and exactly what it entailed was not taken seriously or truly understood, at that time. It was not Raymond’s plan or desire to be a preacher, and he tried to do anything and everything to avoid the talks of him becoming one. Raymond’s path of life, although he believed in God, took him down the road that led him away from God. His struggles with life’s events and being an introvert kept him emotionally troubled, in a state of depression and wanting to commit suicide. Yet, as the Lord was with Jeremiah, even so was the Lord with Raymond. The Lord was to show Raymond just what it meant to have complete trust in Him and to know that He would always provide a way of an escape. Before Raymond came to the point of carrying out his plans to commit suicide, he prayed a simple prayer that God would give him a new family. At that exact moment Raymond’s life began to take a new direction. He began to seek after the Lord; it became his quest to find out what it meant to be a servant of God. Because of his being an introvert, he began to write his emotions on paper in the form of poems. Those poems gave him the strength to come out of depression and began his two year journey to find God.</p>
      <p>Raymond’s relationship with Jesus and salvation journey began at the age of nineteen. The poetry writing started as a therapeutic remedy for his troubled past, but developed into the psalms of Raymond because of God’s grace and mercy that delivered him from despair and hopelessness.</p>
      <p>God’s favor covers Raymond’s life and carries him from day to day. It is written that “without me (Christ) ye can do nothing” (John 15:5). This scripture resonates in Raymond’s heart. For, he truly believes that God is the author and he is just the vessel used of God. His desire is that each poem will be taken personally and become a tool used by everyone to help them on their Christian journey and to let them know that they are never alone in their experience and quest to be closer to the Lord Jesus Christ.</p>
    </div>
  </section>

  <div class="fold fold--left"></div>
  <div class="fold fold--right"></div>

  <section class="spine">
    <div class="spine-title">BENEATH A COPPER EVENING SKY STILL</div>
    <div class="spine-author">RL MOSKOWICZ</div>
  </section>

  <section class="front">
    <div class="front-title title-top">BENEATH A COPPER</div>
    <svg class="cross" width="188" height="420" viewBox="0 0 188 420" aria-hidden="true">
      <polygon points="66,0 128,6 132,418 62,418" fill="var(--cross)"/>
      <rect x="0" y="114" width="188" height="48" fill="var(--cross)"/>
    </svg>
    <div class="front-title title-left">EVENING</div>
    <div class="front-title title-right">SKY</div>
    <div class="front-title title-bottom">STILL</div>
    <div class="tagline">A COMPILATION OF POEMS BY RL MOSKOWICZ</div>
  </section>

  <div class="trim-frame"></div>
</div>
</body>
</html>
```